I would like a new business card designed. I am a kitchen installer for cabinet makers.
I install:
-kitchens
-vanities units
-laundry cabinets
-pantries
-wardrobe shelving
I would like the colors lime green and greys used.
servicing all areas
Also needs to include the words- residential, commercial, industrial
I also want a logo that can be used on work clothes
Modern looking
Target Market(s)
cabinet makers
Industry/Entity Type
Business
Contact Information for Business Card
RJ joinery & fitouts pty ltd
0418729564
rjjfit@mailbox-example.com.au
www.rjjoinery-example.com.au
Logo styles of interest
Emblem Logo
Look and feel

```html
<!DOCTYPE html>
<html lang="en">
<head>
<meta charset="utf-8">
<title>RJ joinery &amp; fitouts pty ltd – Stationery</title>
<link rel="stylesheet" href="https://fonts.googleapis.com/css2?family=Michroma&family=Arimo:wght@400;700&display=swap">
<style>
  :root {
    --lime: #9acb34;
    --grey: #6d6e71;
    --grey-light: #c9c9c9;
    --paper: #ffffff;
    --card-paper: #f1f1ee;
    --backdrop: #e6e6e6;
    --brand-font: "Michroma", sans-serif;
    --body-font: "Arimo", Arial, sans-serif;
  }
  * { box-sizing: border-box; margin: 0; padding: 0; }
  html, body { width: 1200px; height: 940px; overflow: hidden; }
  body { background: var(--backdrop); font-family: var(--body-font); }
  .stage { position: relative; width: 1200px; height: 940px; overflow: hidden; }

  .brand-name {
    font-family: var(--brand-font);
    font-weight: 400;
    line-height: 1.05;
    letter-spacing: 0.02em;
    white-space: nowrap;
  }
  .brand-dot { position: absolute; border-radius: 50%; background: var(--lime); }

  /* Letterhead */
  .letterhead {
    position: absolute; left: 523px; top: 76px; width: 570px; height: 806px;
    background: var(--paper); border: 1px solid var(--grey-light);
  }
  .letterhead .brand-dot { left: 15px; top: 14px; width: 60px; height: 60px; }
  .letterhead .brand-name {
    position: absolute; left: 81px; top: 38px; font-size: 11px; color: var(--lime);
  }
  .letterhead .rule {
    position: absolute; left: 268px; right: 0; top: 57px; height: 1px; background: var(--lime);
  }
  .letterhead .footer-band {
    position: absolute; left: 0; right: 0; bottom: 0; height: 24px; background: var(--lime);
    color: #fff; font-size: 10px; text-align: center; line-height: 24px;
  }

  /* Business card – front */
  .card { position: absolute; width: 245px; height: 149px; overflow: hidden; }
  .card-front { left: 218px; top: 263px; background: var(--card-paper); }
  .card-front .brand-dot { left: -4px; top: -30px; width: 138px; height: 138px; }
  .card-front .brand-name {
    position: absolute; left: 52px; top: 82px; font-size: 11px; color: var(--grey);
  }
  .sector-list { position: absolute; right: 8px; top: 30px; list-style: none; }
  .sector-list li {
    width: 78px; height: 13px; margin-bottom: 6px; background: var(--lime);
    border-radius: 7px 0 0 7px; color: #fff; font-size: 9px; line-height: 13px; text-align: center;
  }
  .card-front .web { position: absolute; left: 0; right: 0; bottom: 4px; text-align: center; font-size: 7px; color: var(--lime); }

  /* Business card – back */
  .card-back { left: 477px; top: 263px; background: var(--lime); color: #fff; }
  .card-back .brand-dot { left: 8px; top: 15px; width: 44px; height: 44px; background: #fff; }
  .card-back .brand-name { position: absolute; left: 56px; top: 25px; font-size: 8px; color: #fff; }
  .card-back .holder { position: absolute; left: 137px; top: 80px; }
  .card-back .holder-name { font-size: 10px; letter-spacing: 0.22em; }
  .card-back .holder-role { font-size: 7px; margin-top: 1px; }
  .card-back .contact { position: absolute; left: 137px; font-size: 5.5px; line-height: 7px; }
  .card-back .contact.phones { top: 109px; }
  .card-back .contact.online { top: 129px; }

  /* Envelope */
  .envelope { position: absolute; left: 71px; top: 461px; width: 611px; height: 362px; }
  .envelope .flap { position: absolute; left: 0; top: 0; }
  .envelope .flap-mark { position: absolute; left: 50%; top: 22px; transform: translateX(-50%) rotate(180deg); width: 150px; height: 50px; }
  .envelope .flap-mark .brand-dot { left: 64px; top: 0; width: 26px; height: 26px; background: #fff; }
  .envelope .flap-mark .brand-name { position: absolute; left: 20px; top: 30px; font-size: 6px; color: #fff; }
  .envelope-body {
    position: absolute; left: 0; top: 95px; width: 611px; height: 267px;
    background: var(--paper); border: 1px solid var(--grey-light); border-top: none;
  }
  .envelope-body .brand-dot { left: 16px; top: 17px; width: 58px; height: 58px; }
  .envelope-body .brand-name { position: absolute; left: 78px; top: 39px; font-size: 11px; color: var(--lime); }
  .envelope-body .window {
    position: absolute; left: 337px; top: 136px; width: 224px; height: 101px;
    border: 1px solid var(--grey-light); border-radius: 16px;
  }
  .envelope-body .contact { position: absolute; left: 12px; top: 246px; font-size: 6.5px; line-height: 8px; color: var(--lime); }
</style>
</head>
<body>
<main class="stage">

  <section class="letterhead">
    <span class="brand-dot"></span>
    <p class="brand-name">RJ joinery<br>&amp; fitouts pty ltd</p>
    <span class="rule"></span>
    <p class="footer-band">www.rjjoinery-example.com.au</p>
  </section>

  <section class="card card-front">
    <span class="brand-dot"></span>
    <p class="brand-name">RJ joinery<br>&amp; fitouts pty ltd</p>
    <ul class="sector-list">
      <li>Residential</li>
      <li>Commercial</li>
      <li>Industrial</li>
    </ul>
    <p class="web">www.rjjoinery-example.com.au</p>
  </section>

  <section class="card card-back">
    <span class="brand-dot"></span>
    <p class="brand-name">RJ joinery<br>&amp; fitouts pty ltd</p>
    <div class="holder">
      <p class="holder-name">Your Name</p>
      <p class="holder-role">Director</p>
    </div>
    <p class="contact phones">T : + 61 2 5550 4821<br>M : + 61 455 730 912</p>
    <p class="contact online">E : rjjfit@mailbox-example.com.au<br>W : www.rjjoinery-example.com.au</p>
  </section>

  <section class="envelope">
    <svg class="flap" width="611" height="100" viewBox="0 0 611 100">
      <path d="M0 96 L0 76 Q0 62 14 60 L305 8 L597 60 Q611 62 611 76 L611 96 Z" fill="var(--lime)"/>
    </svg>
    <div class="flap-mark">
      <span class="brand-dot"></span>
      <p class="brand-name">RJ joinery &amp; fitouts pty ltd</p>
    </div>
    <div class="envelope-body">
      <span class="brand-dot"></span>
      <p class="brand-name">RJ joinery<br>&amp; fitouts pty ltd</p>
      <span class="window"></span>
      <p class="contact">E : rjjfit@mailbox-example.com.au<br>W : www.rjjoinery-example.com.au</p>
    </div>
  </section>

</main>
</body>
</html>
```